Chocolate company needing sticker for products

I have a small chocolate company Willow Bend Sweets in Austin Texas. I make all vegan, gluten free, organic, faire trade chocolate that tastes amazing! It is allergy friendly approvable by all ages. I want to have a great sticker that i can put on our boxes and bags. I am using a lot of natural craft color and brown. I am open to color options possibly for different flavors. I want the packaging to reflect the basis of my company. It is all handmade by me but i don't want it to have to much of a crafty look to it. I have attached the logo designs I have. it the sticker can have som of the bullet points about the company that would be great. But it needs to say Locally Made in Austin Texas. it also has to have the company address.
418 West Cobbler Ridge Rd #207 Austin Tx 78745. These things are required by the state for food regulations. I want something that looks great and I can be really proud to put on my product! Thanks so much for all of your help in advance. Dot

I also need some other information added to the sticker. Website which is willowbendsweetsatx.com 

Phone number 512.368.4175. Instagram willowbendsweets. Thanks for your hard work! 

Industry/Entity Type

Chocolate Company

Requirements
Must have
• The logo is added at the bottom as well as designs I like I want to have a professional look but it to be approvable by all consumers. I will gig feed back as i see what designs come through. This will probably fold out into a multi design project so i will be looking for assistance on other areas of this as well. Thanks

```html
<!DOCTYPE html>
<html lang="en">
<head>
<meta charset="utf-8">
<title>Willow Bend Sweets – Product Sticker</title>
<link rel="stylesheet" href="https://fonts.googleapis.com/css2?family=Oswald:wght@500;700&family=Yellowtail&family=Old+Standard+TT:wght@400;700&display=swap">
<style>
  :root {
    --mint: #a6f7d2;
    --cocoa: #231210;
    --backdrop-center: #ffffff;
    --backdrop-edge: #dfe1e3;
  }
  * { box-sizing: border-box; margin: 0; padding: 0; }
  html, body {
    width: 1200px; height: 900px; overflow: hidden;
  }
  body {
    position: relative;
    background: radial-gradient(ellipse 60% 58% at 50% 50%, var(--backdrop-center) 70%, var(--backdrop-edge) 100%);
  }
  .sticker {
    position: absolute;
    top: 207px;
    width: 456px; height: 456px;
    background: var(--paper);
    color: var(--ink);
  }
  .sticker--mint { left: 87px; --paper: var(--mint); --ink: var(--cocoa); }
  .sticker--cocoa { left: 657px; --paper: var(--cocoa); --ink: var(--mint); }

  .sticker__frame {
    position: absolute; inset: 14px;
    border: 3px dotted var(--ink);
  }
  .sticker__brand {
    position: absolute; left: 0; right: 0; top: 46px;
    text-align: center;
    font-family: "Oswald", sans-serif; font-weight: 500;
    text-transform: uppercase; line-height: 1;
    font-size: 40px; letter-spacing: 1px;
  }
  .sticker__brand span { display: block; }
  .sticker__brand .brand-mid { font-size: 20px; letter-spacing: 3px; margin: 7px 0; }
  .rule {
    position: absolute; left: 68px; width: 336px;
  }
  .rule--solid { top: 210px; border-top: 1.5px solid var(--ink); opacity: .75; }
  .rule--dotted { top: 257px; border-top: 3px dotted var(--ink); }
  .rule--double { top: 320px; height: 4px; border-top: 1.5px solid var(--ink); border-bottom: 1px solid var(--ink); opacity: .75; }
  .sticker__local {
    position: absolute; left: 0; right: 0; top: 210px;
    text-align: center;
    font-family: "Yellowtail", cursive; font-size: 28px; line-height: 1.2;
  }
  .sticker__in {
    position: absolute; left: 0; right: 0; top: 242px;
    text-align: center; font-family: "Yellowtail", cursive; font-size: 15px;
  }
  .sticker__city {
    position: absolute; left: 0; right: 0; top: 262px;
    text-align: center;
    font-family: "Oswald", sans-serif; font-weight: 700;
    font-size: 42px; line-height: 1;
  }
  .address {
    position: absolute; top: 336px; left: 60px; right: 60px;
    display: flex; justify-content: center;
    line-height: 23px;
  }
  .address__street {
    text-align: right; padding-right: 6px;
    font-family: "Oswald", sans-serif; font-weight: 700; font-size: 17px;
  }
  .address__street .num { font-family: "Old Standard TT", serif; font-weight: 400; font-style: italic; }
  .address__divider { border-left: 2px dotted var(--ink); margin: 3px 0; }
  .address__city {
    padding-left: 6px;
    font-family: "Old Standard TT", serif; font-size: 17px;
  }
  .address__city .unit { font-family: "Oswald", sans-serif; font-weight: 700; }
  .address__city .upper { font-weight: 700; letter-spacing: .5px; }
  .address__city svg { vertical-align: -2px; margin-right: 10px; }
  .sticker__flourish {
    position: absolute; left: 168px; top: 390px;
    width: 92px; height: 24px; border-radius: 12px;
    background: var(--ink); opacity: .35;
  }
</style>
</head>
<body>
  <section class="sticker sticker--mint">
    <div class="sticker__frame"></div>
    <h1 class="sticker__brand"><span>Willow</span><span class="brand-mid">Bend</span><span>Sweets</span></h1>
    <div class="rule rule--solid"></div>
    <p class="sticker__local">Locally made</p>
    <div class="rule rule--dotted"></div>
    <p class="sticker__in">in</p>
    <p class="sticker__city">Austin Texas</p>
    <div class="rule rule--double"></div>
    <address class="address">
      <div class="address__street">West Cobbler Ridge<br><span class="num">№</span> 418 Rd</div>
      <div class="address__divider"></div>
      <div class="address__city"><span class="unit">#207</span> <span class="upper">AUSTIN</span><br>
        <svg width="24" height="14" viewBox="0 0 24 14"><path d="M0 4h14V0l10 7-10 7v-4H0z" fill="currentColor"/></svg>Tx 78745</div>
    </address>
    <div class="sticker__flourish" role="img" aria-label="Decorative swash ornament"></div>
  </section>

  <section class="sticker sticker--cocoa">
    <div class="sticker__frame"></div>
    <h1 class="sticker__brand"><span>Willow</span><span class="brand-mid">Bend</span><span>Sweets</span></h1>
    <div class="rule rule--solid"></div>
    <p class="sticker__local">Locally made</p>
    <div class="rule rule--dotted"></div>
    <p class="sticker__in">in</p>
    <p class="sticker__city">Austin Texas</p>
    <div class="rule rule--double"></div>
    <address class="address">
      <div class="address__street">West Cobbler Ridge<br><span class="num">№</span> 418 Rd</div>
      <div class="address__divider"></div>
      <div class="address__city"><span class="unit">#207</span> <span class="upper">AUSTIN</span><br>
        <svg width="24" height="14" viewBox="0 0 24 14"><path d="M0 4h14V0l10 7-10 7v-4H0z" fill="currentColor"/></svg>Tx 78745</div>
    </address>
    <div class="sticker__flourish" role="img" aria-label="Decorative swash ornament"></div>
  </section>
</body>
</html>
```